Cedar Hall businesscard

We changed our name and logo, now we need new business cards.
3-4/72 Marlow Street Larkfield 2999
www.cedarhall-example.org.au
info@cedarhall-example.org.au
Lorna-Jean Whitcombe
Senior Pastor
ph: 02 95874210

```html
<!DOCTYPE html>
<html lang="en">
<head>
<meta charset="utf-8">
<title>Cedar Hall – Business Card</title>
<link rel="stylesheet" href="https://fonts.googleapis.com/css2?family=Exo+2:ital,wght@1,400;1,500;1,600;1,700;1,800;1,900&display=swap">
<style>
  :root {
    --ink: #111111;
    --paper: #fdfdfd;
    --frame: #000000;
    --link-blue: #3b8fd6;
    --wave-light: #4aa6e0;
    --wave-mid: #2e86cc;
    --wave-deep: #1f6fb8;
    --mark-grey: #7d8a96;
  }
  html, body {
    margin: 0;
    padding: 0;
    width: 1200px;
    height: 702px;
    overflow: hidden;
    background: #ffffff;
  }
  .card {
    position: relative;
    width: 1200px;
    height: 702px;
    font-family: "Exo 2", sans-serif;
    font-style: italic;
    color: var(--ink);
  }
  .card-art {
    position: absolute;
    inset: 0;
  }
  .card-title {
    position: absolute;
    left: 0;
    width: 1190px;
    top: 72px;
    margin: 0;
    text-align: center;
    font-size: 80px;
    font-weight: 900;
    letter-spacing: 2px;
    line-height: 1.1;
    text-shadow: 3px 4px 5px rgba(0,0,0,0.35);
  }
  .contact-name {
    position: absolute;
    left: 100px;
    top: 206px;
    margin: 0;
    font-size: 45px;
    font-weight: 800;
    letter-spacing: 1.5px;
    line-height: 1.2;
  }
  .contact-role {
    position: absolute;
    left: 100px;
    top: 258px;
    margin: 0;
    font-size: 39px;
    font-weight: 500;
    letter-spacing: 0.5px;
    line-height: 1.2;
  }
  .address {
    position: absolute;
    left: 106px;
    top: 321px;
    margin: 0;
    font-size: 31px;
    font-weight: 600;
    line-height: 1.2;
  }
  .website {
    position: absolute;
    left: 106px;
    top: 372px;
    margin: 0;
    font-size: 34px;
    font-weight: 600;
    line-height: 1.2;
    color: var(--link-blue);
  }
  .brand {
    position: absolute;
    left: 800px;
    top: 402px;
    display: flex;
    align-items: center;
    gap: 14px;
  }
  .brand-dot {
    width: 34px;
    height: 34px;
    border-radius: 50%;
    background: var(--mark-grey);
  }
  .brand-name {
    font-size: 40px;
    font-weight: 500;
    color: var(--mark-grey);
    letter-spacing: 1px;
  }
  .contact-line {
    position: absolute;
    left: 108px;
    display: flex;
    align-items: center;
    gap: 10px;
    margin: 0;
    font-size: 35px;
    font-weight: 600;
    line-height: 1.2;
    letter-spacing: 0.5px;
    color: var(--ink);
  }
  .contact-line.phone { top: 566px; }
  .contact-line.email { top: 622px; }
  .contact-line svg { flex: none; }
</style>
</head>
<body>
<main class="card">
  <svg class="card-art" width="1200" height="702" viewBox="0 0 1200 702">
    <defs>
      <linearGradient id="waveFill" x1="0" y1="0" x2="1" y2="0.3">
        <stop offset="0" stop-color="var(--wave-mid)"/>
        <stop offset="0.5" stop-color="var(--wave-light)"/>
        <stop offset="1" stop-color="var(--wave-deep)"/>
      </linearGradient>
    </defs>
    <rect class="card-face" x="14" y="13" width="1173" height="676" fill="var(--paper)"/>
    <path class="wave-band" role="img" aria-label="Blue water-texture band along the bottom of the card"
          d="M18 545 Q20 522 60 520 Q400 530 800 580 Q1050 612 1185 645 L1185 688 L18 688 Z"
          fill="url(#waveFill)"/>
    <rect class="card-frame" x="14" y="13" width="1173" height="676" fill="none" stroke="var(--frame)" stroke-width="3"/>
  </svg>

  <h1 class="card-title">Cedar Hall</h1>
  <p class="contact-name">Lorna-Jean Whitcombe</p>
  <p class="contact-role">Senior Pastor</p>
  <p class="address">3-4/72 Marlow Street Larkfield 2999</p>
  <p class="website">www.cedarhall-example.org.au</p>

  <div class="brand">
    <span class="brand-dot"></span>
    <span class="brand-name">Cedar Hall</span>
  </div>

  <p class="contact-line phone">
    <svg width="50" height="36" viewBox="0 0 48 34" aria-hidden="true">
      <path d="M4 12 Q4 3 24 3 Q44 3 44 12 L44 15 L34 15 L34 10 L14 10 L14 15 L4 15 Z" fill="var(--ink)"/>
      <path d="M12 15 L36 15 L42 31 L6 31 Z" fill="var(--ink)"/>
      <circle cx="24" cy="22" r="5" fill="var(--wave-light)"/>
    </svg>
    <span>ph: 02 95874210</span>
  </p>
  <p class="contact-line email">
    <svg width="50" height="30" viewBox="0 0 50 30" aria-hidden="true">
      <rect x="2" y="2" width="46" height="26" fill="none" stroke="var(--ink)" stroke-width="3"/>
      <path d="M2 2 L25 18 L48 2 M2 28 L19 14 M48 28 L31 14" fill="none" stroke="var(--ink)" stroke-width="3"/>
    </svg>
    <span>info@cedarhall-example.org.au</span>
  </p>
</main>
</body>
</html>
```